Holvern Cabinets Quality Custom Built Kitchens, Vanity Units, Robes ect

Hi,
Was after a new design for our business cards,
we are a cabinet making business and pride ourselves in quality custom built Kitchens, Vanity units, robes ect.
we have been around for over 20 years and we are trying to modernize our card logo.
Looking for something eye catching, bold and exciting
family ran and operated business, we work with builders and also have a large private clientel.

Thanks

Industry/Entity Type

Business

Contact Information for Business Card

Holvern Cabinets

Font styles to use
Serif
Script

Requirements
Must have
• Marisol 0461937254 hvcabinets@mailvento.com
• Po Box 2786
• 5C Larkspur Court Traralgon Vic 3917
• Phone (03)52896407 Fax (03) 52896931
Nice to have
• Quality Custom Built Kitchens & Vanity Units

```html
<!DOCTYPE html>
<html lang="en">
<head>
<meta charset="utf-8">
<title>Holvern Cabinets – Business Card</title>
<link href="https://fonts.googleapis.com/css2?family=Russo+One&family=Michroma&family=Open+Sans:wght@400;700&display=swap" rel="stylesheet">
<style>
  :root {
    --brand-blue: #1f4597;
    --ink: #111111;
    --rule-grey: #8a8a8a;
    --card-white: #ffffff;
    --backdrop: #e7e5e2;
  }
  html, body {
    margin: 0;
    width: 1200px;
    height: 1000px;
    overflow: hidden;
    background: var(--backdrop);
  }
  .canvas { position: relative; width: 1200px; height: 1000px; }
  .card {
    position: absolute;
    left: 265px;
    width: 665px;
    height: 397px;
    background: var(--card-white);
    border-radius: 22px;
    overflow: hidden;
    box-shadow: 0 3px 10px rgba(0,0,0,0.18);
  }
  .card--front { top: 73px; }
  .card--back { top: 532px; }

  .brand-mark {
    position: absolute;
    background: var(--brand-blue);
  }
  .card--front .brand-mark { left: 283px; top: 48px; width: 98px; height: 98px; }
  .card--back .brand-mark { left: 269px; top: 87px; width: 126px; height: 126px; }

  .brand {
    position: absolute;
    left: 0; right: 0;
    text-align: center;
  }
  .brand__name {
    font-family: "Russo One", sans-serif;
    color: var(--brand-blue);
    letter-spacing: 0.5px;
    line-height: 1;
    margin: 0;
  }
  .brand__tagline {
    font-family: "Michroma", sans-serif;
    color: var(--ink);
    margin: 0;
    line-height: 1;
  }
  .card--front .brand { top: 176px; }
  .card--front .brand__name { font-size: 29px; }
  .card--front .brand__tagline { font-size: 10.5px; margin-top: 5px; }
  .card--back .brand { top: 250px; }
  .card--back .brand__name { font-size: 37px; }
  .card--back .brand__tagline { font-size: 13.5px; margin-top: 6px; }

  .contact-person {
    position: absolute;
    right: 350px;
    top: 287px;
    text-align: right;
    font-family: "Open Sans", sans-serif;
  }
  .contact-person__name {
    color: var(--brand-blue);
    font-weight: 700;
    font-size: 15px;
    letter-spacing: 0.5px;
    margin: 0 0 3px;
  }
  .contact-person__mobile {
    font-size: 14px;
    color: var(--ink);
    margin: 0;
    display: flex;
    align-items: center;
    gap: 3px;
  }
  .divider {
    position: absolute;
    left: 333px;
    top: 270px;
    width: 1px;
    height: 76px;
    background: var(--rule-grey);
  }
  .contact-list {
    position: absolute;
    left: 351px;
    top: 264px;
    margin: 0;
    padding: 0;
    list-style: none;
    font-family: "Open Sans", sans-serif;
    font-size: 14px;
    color: var(--ink);
    line-height: 17px;
  }
  .contact-list li { display: flex; align-items: center; gap: 5px; white-space: nowrap; }
  .contact-list svg { width: 13px; height: 13px; fill: var(--brand-blue); }
  .contact-list__address { margin-top: 1px; }
  .band-rule {
    position: absolute; left: 0; right: 0; top: 363px; height: 4px;
    background: var(--rule-grey);
  }
  .band {
    position: absolute; left: 0; right: 0; top: 370px; bottom: 0;
    background: var(--brand-blue);
  }
</style>
</head>
<body>
<div class="canvas">
  <section class="card card--front" aria-label="Card front">
    <div class="brand-mark" aria-hidden="true"></div>
    <div class="brand">
      <p class="brand__name">HOLVERN CABINETS</p>
      <p class="brand__tagline">Quality Custom Built Kitchens &amp; Vanity Units</p>
    </div>

    <div class="contact-person">
      <p class="contact-person__name">MARISOL</p>
      <p class="contact-person__mobile">0461937254
        <svg width="12" height="12" viewBox="0 0 24 24" aria-hidden="true"><path fill="#1f4597" d="M6.6 10.8a15 15 0 0 0 6.6 6.6l2.2-2.2a1 1 0 0 1 1-.25 11.4 11.4 0 0 0 3.6.57 1 1 0 0 1 1 1V20a1 1 0 0 1-1 1A17 17 0 0 1 3 4a1 1 0 0 1 1-1h3.5a1 1 0 0 1 1 1c0 1.25.2 2.45.57 3.570a1 1 0 0 1-.25 1z"/></svg>
      </p>
    </div>

    <div class="divider"></div>

    <ul class="contact-list">
      <li><svg viewBox="0 0 24 24" aria-hidden="true"><path d="M2 9c0-3 5-5 10-5s10 2 10 5v2h-5V8H7v3H2zM6 12h12l2 8H4z"/></svg>(03)52896407</li>
      <li><svg viewBox="0 0 24 24" aria-hidden="true"><path d="M6 2h12v6H6zM3 9h18v9h-3v4H6v-4H3zm5 6v5h8v-5z"/></svg>(03) 52896931</li>
      <li><svg viewBox="0 0 24 24" aria-hidden="true"><path d="M2 5h20v14H2zm2 2v.5l8 5 8-5V7z"/></svg>hvcabinets@mailvento.com</li>
      <li class="contact-list__address">Po Box 2786</li>
      <li>5C Larkspur Court Traralgon Vic 3917</li>
    </ul>

    <div class="band-rule"></div>
    <div class="band"></div>
  </section>

  <section class="card card--back" aria-label="Card back">
    <div class="brand-mark" aria-hidden="true"></div>
    <div class="brand">
      <p class="brand__name">HOLVERN CABINETS</p>
      <p class="brand__tagline">Quality Custom Built Kitchens &amp; Vanity Units</p>
    </div>
  </section>
</div>
</body>
</html>
```